Psychotherapist's business card

I need a business card design for a psychotherapist. I expect business card to have "light" design. By this I mean that it can somehow translate easiness, serenity. Maybe pastel colours can help you here. I have attached some pictures from Greece. Perhaps they can inspire you to combine colours and to achieve that "light" design.
Updates

Pls, don't use any free samples you may find on business card generators. It looks too simple, uncreative and waste of time! READ size and colour requirements! I don't want to see any shapes like rings, triangles etc.

Contact Information for Business Card

Size: 65mmX60mm

Name - Вячеслав Мирошенко

Психолог
+7(916)482-30-67
miroshenko.com

I suppose that thin font can look good but it's up to you

Requirements
Must have
• size requirements
Nice to have
• pastel colours
• thin font
Should not have
• black and dark colours
• lines, free design samples used from other web-sites

```html
<!DOCTYPE html>
<html lang="ru">
<head>
<meta charset="utf-8">
<title>Вячеслав Мирошенко — визитка психолога</title>
<link rel="stylesheet" href="https://fonts.googleapis.com/css2?family=Open+Sans:wght@400&display=swap">
<style>
  :root {
    --page-bg: #2e2f31;
    --card-top: #b7dde3;
    --card-bottom: #9ec2c8;
    --ink: #1d6fb3;
  }
  html, body {
    margin: 0;
    padding: 0;
    width: 1200px;
    height: 997px;
    overflow: hidden;
    background: var(--page-bg);
  }
  .canvas {
    position: relative;
    width: 1200px;
    height: 997px;
    display: flex;
    align-items: center;
    justify-content: center;
  }
  .business-card {
    position: relative;
    width: 600px;
    height: 554px;
    background: linear-gradient(160deg, var(--card-top) 0%, var(--card-bottom) 100%);
    font-family: "Open Sans", sans-serif;
    font-weight: 400;
    color: var(--ink);
  }
  .card-role {
    position: absolute;
    left: 150px;
    top: 78px;
    margin: 0;
    font-size: 18px;
    letter-spacing: 0.02em;
  }
  .card-name {
    position: absolute;
    left: 150px;
    top: 200px;
    margin: 0;
    font-size: 34px;
    font-weight: 400;
    line-height: 1.2;
  }
  .card-contacts {
    position: absolute;
    left: 280px;
    top: 418px;
    margin: 0;
    font-style: normal;
    font-size: 20px;
    line-height: 1.45;
    text-align: center;
  }
  .card-contacts span { display: block; }
</style>
</head>
<body>
  <main class="canvas">
    <section class="business-card" aria-label="Визитная карточка психолога">
      <p class="card-role">Психолог</p>
      <h1 class="card-name">Вячеслав<br>Мирошенко</h1>
      <address class="card-contacts">
        <span class="contact-phone">+7(916)482-30-67</span>
        <span class="contact-site">miroshenko.com</span>
      </address>
    </section>
  </main>
</body>
</html>
```